Full Service Outdoor Property Management Company

We are looking for a new and fresh business card design. My company has been in business for 26 years. Winter: We are a large snow and ice management company that does work for commercial, industrial and municipal clients. We have been named "Top 100 Snow Companies in the U.S." for numerous years. Summer: We provide complete landscape maintenance and landscape design and construction for both residential and commercial clients. We must incorporate our logo into card design as well as (in no particular order):
Employees name
Office: (555) 847-2036
Cell: (xxx) xxx-xxxx
thornvale.com
1837 Wrenfield, Alderbrook MI 49990
(Something about 26 + years in business as well as "Top 100 snow contractors as stated above)
Target Market(s)
Winter: Commercial, Industrial, Municipal
Summer: Residential and Commercial
Industry/Entity Type
Construction
Contact Information for Business Card
This is a little challenging as we are using one card for essentially two companies that target different customers from summer to winter. Perhaps the back side could be split in two or something to highlight the different services?? I'm open to any ideas!! Looking forward to seeing what you come up with!
Requirements
Must have
- Logo
- (in no particular order)
- Employees name
- Office: (555) 847-2036
- Cell: (xxx) xxx-xxxx
- thornvale.com
- 1837 Wrenfield, Alderbrook MI 49990
Nice to have
- Something about 26 + years in business
- "Top 100 Snow Contractors in the U.S."
Should not have
- Cheesy pictures of lawn mowers and snow plows

```html
<!DOCTYPE html>
<html lang="en">
<head>
<meta charset="utf-8">
<title>Thornvale Incorporated – Business Card</title>
<link href="https://fonts.googleapis.com/css2?family=Arimo:wght@400&display=swap" rel="stylesheet">
<style>
  :root {
    --bg: #e9e6e2;
    --card: #fcfbfa;
    --green: #14965f;
    --ink: #1c1c1c;
    --snow-light: #f1f2f4;
    --snow-mid: #c9ccd2;
    --tree: #7d8079;
    --faint-warm: #e7ddd6;
  }
  * { box-sizing: border-box; margin: 0; padding: 0; }
  html, body {
    width: 1200px; height: 914px; overflow: hidden;
    background: var(--bg);
    font-family: "Arimo", Arial, sans-serif;
  }
  .card {
    position: absolute;
    left: 290px;
    width: 620px; height: 354px;
    background: var(--card);
    box-shadow: 0 4px 14px rgba(0,0,0,0.15);
    overflow: hidden;
  }
  .card--front { top: 60px; }
  .card--back  { top: 500px; }

  .front-photo { position: absolute; left: 0; top: 0; }

  .front-info {
    position: absolute;
    left: 240px; top: 52px; width: 360px;
    text-align: center;
    color: var(--ink);
  }
  .company-name {
    color: var(--green);
    font-size: 34px;
    line-height: 1.15;
    white-space: nowrap;
  }
  .employee-name {
    color: var(--green);
    font-size: 24px;
    margin-top: 34px;
  }
  .contact-lines {
    list-style: none;
    font-size: 17px;
    line-height: 1.5;
    margin-top: 12px;
  }

  .back-photo {
    position: absolute; inset: 0;
    background:
      radial-gradient(ellipse at 55% 45%, var(--faint-warm) 0%, rgba(231,221,214,0) 60%),
      linear-gradient(180deg, #eeeeef 0%, var(--snow-light) 100%);
  }
  .back-content {
    position: absolute;
    left: 0; right: 0; top: 112px;
    text-align: center;
  }
  .back-content .company-name { font-size: 40px; }
  .tagline {
    margin-top: 40px;
    font-size: 21px;
    color: var(--ink);
  }
</style>
</head>
<body>

<section class="card card--front" aria-label="Business card front">
  <svg class="front-photo" width="620" height="354" viewBox="0 0 620 354">
    <defs>
      <linearGradient id="snowScene" x1="0" y1="0" x2="0" y2="1">
        <stop offset="0" stop-color="#cfd2d6"/>
        <stop offset="0.3" stop-color="#7d8079"/>
        <stop offset="0.42" stop-color="#f1f2f4"/>
        <stop offset="1" stop-color="#c9ccd2"/>
      </linearGradient>
    </defs>
    <path role="img" aria-label="Photo of a snow plow clearing a snowy lot"
          d="M0 0 H215 Q70 170 118 354 H0 Z" fill="url(#snowScene)"/>
    <path d="M215 0 Q70 170 118 354" fill="none" stroke="#14965f" stroke-width="5"/>
  </svg>

  <div class="front-info">
    <div class="company-name">Thornvale Incorporated</div>
    <div class="employee-name">Employees name</div>
    <ul class="contact-lines">
      <li>(555) 847-2036</li>
      <li>(xxx) xxx-xxxx</li>
      <li>thornvale.com</li>
      <li>1837 Wrenfield, Alderbrook MI 49990</li>
    </ul>
  </div>
</section>

<section class="card card--back" aria-label="Business card back">
  <div class="back-photo" role="img" aria-label="Faded photo of a snow plow tractor in the snow"></div>
  <div class="back-content">
    <div class="company-name">Thornvale Incorporated</div>
    <p class="tagline">"Top 100 Snow Contractors in the U.S."</p>
  </div>
</section>

</body>
</html>
```